Retail Package for Ammunition Company

We are looking for a packaging design for a retail boxed ammunition. The "look". Attached will be the logo to be used. The logo is attached and a can be manipulated on the box. Box to represent strength and accuracy. Will need to provide .psd files to allow in house personnel to add/remove text to other calibers and warnings. Wow me with your designs!

Browse Other Brands: http://www.brightfalconstore.com/brands

The packaging needs to include:
Logo- provided and the following text:

FRONT 1. 9mm 115gr FMJ

BACK 2. WARNING: To avoid serious injury: (1) use only ammunition in good condition; use only in modern firearms in good condition marked for .22 Long Rifle (LR) cartridges; (2) always be sure barrel is free of any obstructions; the barrel should be checked in case of light recoil, or an unusually loud or weak sound heard during firing; (3) wear eye and ear protection; (4) if gun fails to fire, avoid exposure to breech when unloading and point muzzle in a safe direction. Keep firearm pointed in safe direction at all times; (5) discharge may occur if rim is struck; handle with caution, do not drop. (6) Do not shoot at hard surfaces or water to prevent ricochet; (7) Bullet is capable of traveling extreme distances. Know your backstop; (8) Store in cool dry place

3. LEAD WARNING: Discharging firearms in poorly ventilated areas, cleaning firearms, or handling ammunition may result in exposure to lead and other substances known to cause birth defects, reproductive harm, and other serious physical injury. Have adequate ventilation at all times. Wash hands thoroughly after exposure.

Dimensions ; (LxWxH): 5.25" x 2.625" x 1.125"

Target Market(s)

Ammunition Industry

```html
<!DOCTYPE html>
<html lang="en">
<head>
<meta charset="utf-8">
<title>Granite Line – 9 mm Retail Box</title>
<link rel="stylesheet" href="https://fonts.googleapis.com/css2?family=Montserrat:wght@300;400;700&family=Roboto+Condensed:wght@300&display=swap">
<style>
  :root {
    --paper: #ffffff;
    --panel-light: #dedede;
    --panel-dark: #141213;
    --brand-red: #8e1a1c;
    --ink-dark: #2a2a2a;
    --ink-light: #f2f2f2;
    --mark-faint: #3b3a3b;
  }
  * { margin: 0; padding: 0; box-sizing: border-box; }
  html, body { width: 1200px; height: 2979px; overflow: hidden; background: var(--paper); }
  body { position: relative; font-family: "Montserrat", sans-serif; }

  .box-row { position: absolute; left: 260px; display: flex; height: 280px; }
  .panel { position: relative; height: 280px; overflow: hidden; }
  .panel svg.panel-art { position: absolute; inset: 0; }
  .panel-main { width: 560px; }
  .panel-end { width: 120px; }

  .brand {
    position: absolute; display: flex; align-items: center; gap: 12px;
    color: var(--ink-dark); font-weight: 700; line-height: 1;
  }
  .brand-square { width: 16px; height: 16px; background: var(--brand-red); flex: none; }
  .brand-name { font-size: 30px; letter-spacing: 1px; white-space: nowrap; }

  .front .brand { left: 175px; top: 42px; }
  .back .brand { left: 160px; top: 24px; }
  .back .brand-name { font-size: 26px; }

  .caliber-line {
    position: absolute; right: 40px; bottom: 34px;
    color: var(--ink-light); font-weight: 300; font-size: 31px; letter-spacing: 0.5px; white-space: nowrap;
  }
  .caliber-line .sep { font-size: 20px; margin: 0 14px; vertical-align: 4px; }

  .end-label {
    position: absolute; left: 10px; top: 14px;
    color: var(--ink-dark); font-weight: 400; font-size: 16px; line-height: 1.45;
  }

  .warning {
    position: absolute; left: 16px; right: 16px; top: 92px;
    font-family: "Roboto Condensed", sans-serif; font-weight: 300;
    color: var(--ink-light); font-size: 10.5px; line-height: 1.25; text-align: justify;
  }
  .warning p + p { margin-top: 10px; }
</style>
</head>
<body>

<!-- Row 1: end + front -->
<div class="box-row" style="top:320px">
  <div class="panel panel-end">
    <svg class="panel-art" viewBox="0 0 120 280" width="120" height="280">
      <rect width="120" height="280" fill="var(--panel-dark)"/>
      <polygon points="0,0 120,0 120,103 0,140" fill="var(--panel-light)"/>
    </svg>
    <div class="end-label">9 mm<br>115gr FMJ</div>
  </div>
  <div class="panel panel-main front">
    <svg class="panel-art" viewBox="0 0 560 280" width="560" height="280">
      <rect width="560" height="280" fill="var(--panel-dark)"/>
      <polygon points="0,0 560,0 560,112 340,162 0,103" fill="var(--panel-light)"/>
      <polygon points="0,103 340,162 560,112 560,121 340,178 0,108" fill="var(--brand-red)"/>
      <circle cx="72" cy="200" r="44" fill="var(--mark-faint)" role="img" aria-label="Faint brand emblem decoration"/>
    </svg>
    <div class="brand"><span class="brand-square"></span><span class="brand-name">GRANITE LINE</span></div>
    <div class="caliber-line">9 mm<span class="sep">◆</span>115gr FMJ</div>
  </div>
</div>

<!-- Row 2: back + end -->
<div class="box-row" style="top:820px">
  <div class="panel panel-main back">
    <svg class="panel-art" viewBox="0 0 560 280" width="560" height="280">
      <rect width="560" height="280" fill="var(--panel-dark)"/>
      <rect width="560" height="80" fill="var(--panel-light)"/>
    </svg>
    <div class="brand"><span class="brand-square"></span><span class="brand-name">GRANITE LINE</span></div>
    <div class="warning">
      <p>WARNING: To avoid serious injury: (1) use only ammunition in good condition; use only in modern firearms in good condition marked for .22 Long Rifle (LR) cartridges; (2) always be sure barrel is free of any obstructions; the barrel should be checked in case of light recoil, or an unusually loud or weak sound heard during firing; (3) wear eye and ear protection; (4) if gun fails to fire, avoid exposure to breech when unloading and point muzzle in a safe direction. Keep firearm pointed in safe direction at all times; (5) discharge may occur if rim is struck; handle with caution, do not drop. (6) Do not shoot at hard surfaces or water to prevent ricochet; (7) Bullet is capable of traveling extreme distances. Know your backstop; (8) Store in cool dry place</p>
      <p>LEAD WARNING: Discharging firearms in poorly ventilated areas, cleaning firearms, or handling ammunition may result in exposure to lead and other substances known to cause birth defects, reproductive harm, and other serious physical injury. Have adequate ventilation at all times. Wash hands thoroughly after exposure.</p>
    </div>
  </div>
  <div class="panel panel-end">
    <svg class="panel-art" viewBox="0 0 120 280" width="120" height="280">
      <rect width="120" height="280" fill="var(--panel-dark)"/>
      <polygon points="0,0 120,0 120,80 0,100" fill="var(--panel-light)"/>
      <circle cx="100" cy="200" r="36" fill="var(--mark-faint)" role="img" aria-label="Faint brand emblem decoration"/>
    </svg>
    <div class="end-label">9 mm<br>115gr FMJ</div>
  </div>
</div>

<!-- Row 3: end + back -->
<div class="box-row" style="top:1320px">
  <div class="panel panel-end">
    <svg class="panel-art" viewBox="0 0 120 280" width="120" height="280">
      <rect width="120" height="280" fill="var(--panel-dark)"/>
      <polygon points="0,0 120,0 120,80 0,112" fill="var(--panel-light)"/>
      <circle cx="30" cy="200" r="36" fill="var(--mark-faint)" role="img" aria-label="Faint brand emblem decoration"/>
    </svg>
    <div class="end-label">9 mm<br>115gr FMJ</div>
  </div>
  <div class="panel panel-main back">
    <svg class="panel-art" viewBox="0 0 560 280" width="560" height="280">
      <rect width="560" height="280" fill="var(--panel-dark)"/>
      <rect width="560" height="80" fill="var(--panel-light)"/>
    </svg>
    <div class="brand"><span class="brand-square"></span><span class="brand-name">GRANITE LINE</span></div>
    <div class="warning">
      <p>WARNING: To avoid serious injury: (1) use only ammunition in good condition; use only in modern firearms in good condition marked for .22 Long Rifle (LR) cartridges; (2) always be sure barrel is free of any obstructions; the barrel should be checked in case of light recoil, or an unusually loud or weak sound heard during firing; (3) wear eye and ear protection; (4) if gun fails to fire, avoid exposure to breech when unloading and point muzzle in a safe direction. Keep firearm pointed in safe direction at all times; (5) discharge may occur if rim is struck; handle with caution, do not drop. (6) Do not shoot at hard surfaces or water to prevent ricochet; (7) Bullet is capable of traveling extreme distances. Know your backstop; (8) Store in cool dry place</p>
      <p>LEAD WARNING: Discharging firearms in poorly ventilated areas, cleaning firearms, or handling ammunition may result in exposure to lead and other substances known to cause birth defects, reproductive harm, and other serious physical injury. Have adequate ventilation at all times. Wash hands thoroughly after exposure.</p>
    </div>
  </div>
</div>

<!-- Row 4: front + end -->
<div class="box-row" style="top:1820px">
  <div class="panel panel-main front">
    <svg class="panel-art" viewBox="0 0 560 280" width="560" height="280">
      <rect width="560" height="280" fill="var(--panel-dark)"/>
      <polygon points="0,0 560,0 560,112 340,162 0,103" fill="var(--panel-light)"/>
      <polygon points="0,103 340,162 560,112 560,121 340,178 0,108" fill="var(--brand-red)"/>
      <circle cx="72" cy="200" r="44" fill="var(--mark-faint)" role="img" aria-label="Faint brand emblem decoration"/>
    </svg>
    <div class="brand"><span class="brand-square"></span><span class="brand-name">GRANITE LINE</span></div>
    <div class="caliber-line">9 mm<span class="sep">◆</span>115gr FMJ</div>
  </div>
  <div class="panel panel-end">
    <svg class="panel-art" viewBox="0 0 120 280" width="120" height="280">
      <rect width="120" height="280" fill="var(--panel-dark)"/>
      <polygon points="0,0 120,0 120,80 0,112" fill="var(--panel-light)"/>
      <circle cx="70" cy="200" r="36" fill="var(--mark-faint)" role="img" aria-label="Faint brand emblem decoration"/>
    </svg>
    <div class="end-label">9 mm<br>115gr FMJ</div>
  </div>
</div>

<!-- Row 5: front + end -->
<div class="box-row" style="top:2330px">
  <div class="panel panel-main front">
    <svg class="panel-art" viewBox="0 0 560 280" width="560" height="280">
      <rect width="560" height="280" fill="var(--panel-dark)"/>
      <polygon points="0,0 560,0 560,112 340,162 0,103" fill="var(--panel-light)"/>
      <polygon points="0,103 340,162 560,112 560,121 340,178 0,108" fill="var(--brand-red)"/>
      <circle cx="72" cy="200" r="44" fill="var(--mark-faint)" role="img" aria-label="Faint brand emblem decoration"/>
    </svg>
    <div class="brand"><span class="brand-square"></span><span class="brand-name">GRANITE LINE</span></div>
    <div class="caliber-line">9 mm<span class="sep">◆</span>115gr FMJ</div>
  </div>
  <div class="panel panel-end">
    <svg class="panel-art" viewBox="0 0 120 280" width="120" height="280">
      <rect width="120" height="280" fill="var(--panel-dark)"/>
      <polygon points="0,0 120,0 120,80 0,112" fill="var(--panel-light)"/>
      <circle cx="70" cy="200" r="36" fill="var(--mark-faint)" role="img" aria-label="Faint brand emblem decoration"/>
    </svg>
    <div class="end-label">9 mm<br>115gr FMJ</div>
  </div>
</div>

</body>
</html>
```